Design a Pull Up Banner for Finance Broker Business

Pull up banner design. Dimensions 850 x 2000 mm for finance broker . Vertical standing banner will be on display at open homes, auctions and trade shows. Want it to match coporate colours, included logo and look cheerful / breezy with relevant images/ theme for housing / home ownership. Include contact details and text stating Name "Brightvale Financial Solutions" with something like "helping you achieve your financial goals". Include contact number 1300 42 63 51
website address www.brightvale.com.au
email info@brightvale.com.au
Target Market(s)
People seeking finance for home purchases, investment properties, asset finance - motor vehicles and business finance
Industry/Entity Type
Business
Requirements
Must have
- Business Name
- Contact number 1300 42 63 51
- email address info@brightvale.com.au
- Point form of what I do
Nice to have
- Catchy title about the service I provide
- Cheerful image - that match colours of business on website / logo
Should not have
- Too squashy

```html
<!DOCTYPE html>
<html lang="en">
<head>
<meta charset="utf-8">
<title>Brightvale Financial Solutions – Pull Up Banner</title>
<link href="https://fonts.googleapis.com/css2?family=Montserrat:wght@500;600;700;800&display=swap" rel="stylesheet">
<style>
  :root {
    --page-bg: #e9eaec;
    --panel-bg: #dfe6f1;
    --brand-blue: #0b56a8;
    --brand-blue-dark: #0a3f80;
    --accent-blue: #3a9df3;
    --ink: #111418;
    --sky: #3f86d8;
    --lawn: #3f8a2a;
  }
  * { box-sizing: border-box; margin: 0; padding: 0; }
  html, body { width: 1200px; height: 1000px; overflow: hidden; }
  body { background: var(--page-bg); font-family: "Montserrat", Arial, sans-serif; position: relative; }

  .banner {
    position: absolute; left: 421px; top: 53px;
    width: 358px; height: 893px;
    background: var(--panel-bg);
    box-shadow: 0 6px 24px rgba(0,0,0,0.25);
    overflow: hidden;
  }
  .band-top { position: absolute; left: 0; top: 0; width: 100%; height: 36px; background: var(--brand-blue); }
  .band-top::after { content: ""; position: absolute; left: 0; bottom: -5px; width: 100%; height: 2px; background: var(--ink); }

  .brand {
    position: absolute; top: 104px; left: 0; width: 100%;
    display: flex; align-items: center; justify-content: center; gap: 10px;
    font-family: "Montserrat", Arial, sans-serif; font-weight: 700; color: var(--ink);
  }
  .brand-mark { width: 14px; height: 14px; border-radius: 50%; background: var(--brand-blue); flex: none; }
  .brand-text { text-align: left; }
  .brand-name { font-size: 30px; line-height: 1; letter-spacing: 0.3px; }
  .brand-sub { font-size: 12.5px; line-height: 1; margin-top: 6px; letter-spacing: 0.2px; }

  .swoosh { position: absolute; left: 0; top: 178px; width: 358px; height: 60px; z-index: 2; }

  .photo {
    position: absolute; left: 0; top: 209px; width: 100%; height: 316px;
    background: linear-gradient(180deg, var(--sky) 0%, #8fbde8 35%, #9aa6b4 55%, #5f9a3a 72%, var(--lawn) 100%);
  }
  .band-mid { position: absolute; left: 0; top: 525px; width: 100%; height: 14px; background: var(--brand-blue); }

  .headline { position: absolute; top: 554px; left: 0; width: 100%; text-align: center; font-weight: 800; font-size: 37px; line-height: 38px; letter-spacing: 0.3px; }
  .headline .light { color: var(--accent-blue); }
  .headline .dark { color: var(--ink); }
  .rule { position: absolute; top: 675px; left: 30px; width: 298px; height: 2px; background: var(--ink); }

  .tagline { position: absolute; top: 683px; left: 0; width: 100%; text-align: center; font-weight: 500; font-size: 18px; line-height: 24px; color: var(--ink); }

  .services {
    position: absolute; top: 738px; left: 28px; width: 302px;
    list-style: none; display: grid; grid-template-columns: 1fr 1fr; column-gap: 8px; row-gap: 2px;
    font-weight: 600; font-size: 12px; line-height: 15px; color: var(--brand-blue-dark);
  }
  .services li { display: flex; align-items: center; gap: 6px; white-space: nowrap; }
  .services li::before { content: ""; width: 6px; height: 6px; border-radius: 50%; background: var(--accent-blue); flex: none; }

  .contact { position: absolute; top: 779px; left: 0; width: 100%; text-align: center; color: var(--ink); }
  .phone { font-weight: 700; font-size: 27px; color: var(--brand-blue-dark); letter-spacing: 0.5px; line-height: 30px; }
  .email { font-weight: 500; font-size: 15px; line-height: 18px; }
  .web { font-weight: 700; font-size: 15px; line-height: 18px; }
  .web .domain { color: var(--brand-blue); }

  .band-bottom { position: absolute; left: 0; bottom: 0; width: 100%; height: 33px; background: var(--brand-blue); }
  .band-bottom::before { content: ""; position: absolute; left: 0; top: -5px; width: 100%; height: 2px; background: var(--ink); }
</style>
</head>
<body>
  <main class="banner">
    <div class="band-top"></div>

    <div class="brand">
      <span class="brand-mark" aria-hidden="true"></span>
      <div class="brand-text">
        <div class="brand-name">Brightvale</div>
        <div class="brand-sub">Financial Solutions Pty Ltd</div>
      </div>
    </div>

    <svg class="swoosh" viewBox="0 0 358 60" aria-hidden="true">
      <path d="M0 42 C90 22 220 8 358 14 L358 22 C230 18 110 28 0 52 Z" fill="#111418"/>
      <path d="M0 54 C110 30 240 22 358 26 L358 34 C240 32 120 40 0 60 Z" fill="#0b56a8"/>
    </svg>

    <div class="photo" role="img" aria-label="Photo of a sunny suburban street with two-storey family homes, a young tree, a letterbox and a green lawn"></div>
    <div class="band-mid"></div>

    <h1 class="headline">
      <span class="light">BRIGHTVALE</span><br>
      <span class="dark">FINANCIAL</span><br>
      <span class="light">SOLUTIONS</span>
    </h1>
    <div class="rule"></div>

    <p class="tagline">Helping you achieve your<br>Financial Goals</p>

    <ul class="services">
      <li>Home Loans</li>
      <li>Investment Property</li>
      <li>Vehicle &amp; Asset Finance</li>
      <li>Business Finance</li>
    </ul>

    <div class="contact">
      <p class="phone">1300 42 63 51</p>
      <p class="email">info@brightvale.com.au</p>
      <p class="web">www.<span class="domain">brightvale.com</span>.au</p>
    </div>

    <div class="band-bottom"></div>
  </main>
</body>
</html>
```